Banner Ad Needed For Real Estate Lending Firm

We are taking out a banner ad on one of the most highly trafficked real estate websites in New York. The ad will be 970x250. Display format will be JPEG or animated GIF, but original art files will be required as well from the winning designer.

Harbor Ridge Lending (or HRL) is one of the largest "hard money lenders" for real estate investors on the East Coast of the US. We lend for the following real estate investments: 1) Fix And Flip 2) New Construction 3) Cash Out Refinance. We close in 2-10 days. More information can be found on our website here: http://www.hrl7-example.net/

Our goal is to help small business owners, real estate investors, and commercial contractors quickly and efficiently finance their business activities. Our local hard money loan programs are tailored to your unique project needs. We fund fix and flip, new construction, and cash out refinance projects for non-owner occupied properties.

Target Market(s)

Real Estate Agents, Real Estate Investors, Mortgage Brokers, Other Real Estate Professionals

Industry/Entity Type

Real Estate

Font styles to use
Sans Serif

Requirements
Must have
• Must incorporate the fact that we close deals very fast (2 - 10 days), finance the following these 2 main types of investments (Fix and Flip, New Construction), and mention that Brokers can make up to 2.5 Points.
• See attached style guide for basic colors and fonts.
Nice to have
• Animated GIF might be a great feature!

```html
<!DOCTYPE html>
<html lang="en">
<head>
<meta charset="utf-8">
<title>Harbor Ridge Lending – Hard Money Lenders Banner</title>
<link rel="stylesheet" href="https://fonts.googleapis.com/css2?family=Roboto+Condensed:wght@400;500&family=Montserrat:wght@600&display=swap">
<style>
  :root {
    --teal: #0c6276;
    --teal-deep: #074f61;
    --mint: #1fc897;
    --mint-dark: #13b184;
    --ink: #1b1b1b;
    --slate: #2c5c69;
    --ring: #4b907f;
    --paper: #ffffff;
    --stage: #eceff1;
  }
  html, body {
    margin: 0;
    width: 1200px;
    height: 1200px;
    overflow: hidden;
    background: var(--stage);
  }
  .banner {
    position: absolute;
    left: 40px;
    top: 456px;
    width: 1120px;
    height: 288px;
    display: block;
  }
  .headline-top { font-family: "Roboto Condensed", sans-serif; font-weight: 500; fill: var(--mint); }
  .headline-main { font-family: "Roboto Condensed", sans-serif; font-weight: 500; fill: var(--paper); }
  .tagline { font-family: "Roboto Condensed", sans-serif; font-weight: 400; fill: var(--mint); }
  .broker-note { font-family: "Roboto Condensed", sans-serif; font-weight: 500; fill: var(--paper); }
  .service-item { font-family: "Roboto Condensed", sans-serif; font-weight: 500; fill: var(--ink); }
  .cta-label { font-family: "Montserrat", sans-serif; font-weight: 600; fill: var(--paper); letter-spacing: 3px; }
  .brand-name { font-family: "Roboto Condensed", sans-serif; font-weight: 500; fill: var(--slate); letter-spacing: 0.5px; }
</style>
</head>
<body>
<svg class="banner" viewBox="0 0 1251 322" xmlns="http://www.w3.org/2000/svg" aria-label="Harbor Ridge Lending hard money lenders banner">
  <defs>
    <radialGradient id="teal-field" cx="0.35" cy="0.5" r="0.7">
      <stop offset="0" stop-color="var(--teal)"/>
      <stop offset="1" stop-color="var(--teal-deep)"/>
    </radialGradient>
    <linearGradient id="photo-tone" x1="0" y1="0" x2="1" y2="1">
      <stop offset="0" stop-color="#eef1f3"/>
      <stop offset="0.5" stop-color="#c9d3d8"/>
      <stop offset="1" stop-color="#6aa9c9"/>
    </linearGradient>
    <linearGradient id="cta-fill" x1="0" y1="0" x2="0" y2="1">
      <stop offset="0" stop-color="var(--mint)"/>
      <stop offset="1" stop-color="var(--mint-dark)"/>
    </linearGradient>
    <linearGradient id="panel-fill" x1="0" y1="0" x2="0" y2="1">
      <stop offset="0" stop-color="#ffffff"/>
      <stop offset="1" stop-color="#eceeef"/>
    </linearGradient>
    <clipPath id="banner-clip"><rect width="1251" height="322"/></clipPath>
  </defs>

  <g clip-path="url(#banner-clip)">
    <rect class="backdrop" width="1251" height="322" fill="var(--paper)"/>
    <ellipse class="teal-field" cx="620" cy="161" rx="611" ry="441" fill="url(#teal-field)"/>

    <!-- services panel -->
    <rect class="services-panel" x="323" y="53" width="300" height="150" rx="8" fill="url(#panel-fill)" stroke="var(--mint)" stroke-width="2"/>
    <circle cx="345" cy="92" r="6" fill="var(--teal)"/>
    <text class="service-item" x="360" y="102" font-size="30" textLength="124" lengthAdjust="spacingAndGlyphs">Fix And Flip</text>
    <circle cx="345" cy="130" r="6" fill="var(--teal)"/>
    <text class="service-item" x="360" y="140" font-size="30" textLength="188" lengthAdjust="spacingAndGlyphs">New Construction</text>
    <circle cx="345" cy="168" r="6" fill="var(--teal)"/>
    <text class="service-item" x="360" y="178" font-size="30" textLength="204" lengthAdjust="spacingAndGlyphs">Cash Out Refinance</text>

    <!-- broker message -->
    <text class="broker-note" x="330" y="229" font-size="20" textLength="220" lengthAdjust="spacingAndGlyphs">Brokers earn up to 2.5 Points</text>

    <!-- photo area -->
    <circle cx="790" cy="161" r="214" fill="var(--paper)"/>
    <circle cx="790" cy="161" r="213" fill="none" stroke="var(--mint)" stroke-width="4"/>
    <g role="img" aria-label="Photo of a smiling couple holding up the keys to their new home">
      <circle cx="790" cy="161" r="206" fill="url(#photo-tone)"/>
    </g>

    <!-- brand circle -->
    <ellipse class="brand-circle" cx="1086" cy="161" rx="145" ry="186" fill="var(--paper)" stroke="var(--ring)" stroke-width="3"/>
    <text class="brand-name" x="1086" y="145" font-size="20" text-anchor="middle">HARBOR</text>
    <text class="brand-name" x="1086" y="170" font-size="20" text-anchor="middle">RIDGE</text>
    <text class="brand-name" x="1086" y="195" font-size="20" text-anchor="middle">LENDING LLC</text>

    <!-- headline -->
    <text class="headline-top" x="66" y="94" font-size="58" textLength="237" lengthAdjust="spacingAndGlyphs">HARD MONEY</text>
    <text class="headline-main" x="66" y="165" font-size="84" textLength="233" lengthAdjust="spacingAndGlyphs">LENDERS</text>
    <text class="tagline" x="51" y="201" font-size="31" textLength="236" lengthAdjust="spacingAndGlyphs">We close in 2-10 days</text>

    <!-- call to action -->
    <rect class="cta-button" x="79" y="242" width="439" height="46" rx="23" fill="url(#cta-fill)"/>
    <text class="cta-label" x="298.5" y="273" font-size="20" text-anchor="middle" textLength="390" lengthAdjust="spacingAndGlyphs">VISIT US: WWW.HRL7-EXAMPLE.NET</text>
  </g>
</svg>
</body>
</html>
```